New Signage Design Project

Real estate company looking for signage, PowerPoint and stationery branding. Signs will be placed in front of homes and other properties being sold

Name of company is Birch Crest, LLC

Requirements
Must have
• Name of company - Birch Crest, LLC

```html
<!DOCTYPE html>
<html lang="en">
<head>
<meta charset="UTF-8">
<title>Birch Crest, LLC – Sold Sign</title>
<link rel="stylesheet" href="https://fonts.googleapis.com/css2?family=Montserrat:wght@500;700;800&display=swap">
<style>
  :root {
    --charcoal: #222b2c;
    --coral: #e2505c;
    --white: #ffffff;
  }
  * { margin: 0; padding: 0; box-sizing: border-box; }
  html, body { width: 900px; height: 1200px; overflow: hidden; background: var(--charcoal); }
  .sign {
    position: relative;
    width: 900px;
    height: 1200px;
    background: var(--charcoal);
    font-family: "Montserrat", Arial, sans-serif;
    color: var(--white);
    overflow: hidden;
  }
  .sign-backdrop { position: absolute; inset: 0; }
  .status {
    position: absolute;
    top: 38px;
    width: 100%;
    text-align: center;
    font-weight: 800;
    font-size: 258px;
    letter-spacing: -4px;
    line-height: 1;
  }
  .brand {
    position: absolute;
    top: 470px;
    width: 100%;
    display: flex;
    flex-direction: column;
    align-items: center;
  }
  .brand-mark {
    width: 130px;
    height: 130px;
    border-radius: 50%;
    background: var(--white);
  }
  .brand-name {
    margin-top: 80px;
    font-weight: 700;
    font-size: 46px;
    letter-spacing: 1px;
    line-height: 1;
  }
  .agent-name {
    position: absolute;
    top: 818px;
    width: 100%;
    text-align: center;
    font-weight: 500;
    font-size: 100px;
    letter-spacing: 1px;
    line-height: 1;
  }
  .phone-pill {
    position: absolute;
    left: 64px;
    top: 934px;
    width: 773px;
    height: 114px;
    border-radius: 57px;
    background: var(--white);
    display: flex;
    align-items: center;
  }
  .phone-icon {
    width: 124px;
    height: 124px;
    margin-left: -4px;
    flex-shrink: 0;
  }
  .phone-number {
    margin-left: 22px;
    font-weight: 800;
    font-size: 86px;
    letter-spacing: -2px;
    color: var(--coral);
    line-height: 1;
  }
  .footer {
    position: absolute;
    top: 1100px;
    width: 100%;
    display: flex;
    justify-content: center;
    align-items: center;
    gap: 20px;
    font-weight: 500;
    font-size: 36px;
  }
  .footer-url { display: flex; align-items: center; gap: 12px; }
  .footer-divider { width: 2px; height: 44px; background: var(--white); }
  .badges { display: flex; gap: 14px; }
  .badge { width: 44px; height: 44px; background: var(--white); }
</style>
</head>
<body>
<main class="sign">
  <svg class="sign-backdrop" width="900" height="1200" viewBox="0 0 900 1200">
    <polygon points="0,535 451,373 900,535 900,981 0,981" fill="var(--coral)"/>
    <polyline points="0,518 451,303 900,514" fill="none" stroke="var(--white)" stroke-width="7"/>
    <polyline points="0,535 451,373 900,535" fill="none" stroke="var(--white)" stroke-width="4"/>
  </svg>

  <h1 class="status">SOLD</h1>

  <div class="brand">
    <div class="brand-mark"></div>
    <p class="brand-name">BIRCH CREST, LLC</p>
  </div>

  <p class="agent-name">ALEX MORGAN</p>

  <div class="phone-pill">
    <svg class="phone-icon" viewBox="0 0 124 124" aria-hidden="true">
      <circle cx="62" cy="62" r="58" fill="var(--white)" stroke="var(--coral)" stroke-width="5"/>
      <path d="M40 36 l10 -4 l10 16 l-7 6 q5 12 16 18 l6 -7 l16 10 l-4 10 q-4 6 -12 4 q-24 -8 -38 -34 q-4 -10 3 -19z"
            fill="none" stroke="var(--coral)" stroke-width="4" stroke-linejoin="round"/>
      <path d="M66 42 a14 14 0 0 1 14 14 M66 32 a24 24 0 0 1 24 24 M66 22 a34 34 0 0 1 34 34"
            fill="none" stroke="var(--coral)" stroke-width="4" stroke-linecap="round"/>
    </svg>
    <span class="phone-number">0198 765 432</span>
  </div>

  <footer class="footer">
    <span class="footer-url">
      <svg width="32" height="32" viewBox="0 0 32 32" aria-hidden="true">
        <g fill="none" stroke="var(--white)" stroke-width="2.5">
          <circle cx="16" cy="16" r="13"/>
          <ellipse cx="16" cy="16" rx="6" ry="13"/>
          <line x1="3" y1="16" x2="29" y2="16"/>
          <line x1="5" y1="9" x2="27" y2="9"/>
          <line x1="5" y1="23" x2="27" y2="23"/>
        </g>
      </svg>
      www.birchcresthomes.com
    </span>
    <span class="footer-divider"></span>
    <span class="badges">
      <span class="badge"></span>
      <span class="badge"></span>
    </span>
  </footer>
</main>
</body>
</html>
```